Top header for website

Header for website Size is 1000px x 120px
I have CS5 so will need the source files photoshop, illustrator etc, so I can change text and photos.
Photos attached, includes example header and screenshot of eg site
Brief:
I need a website header for golfers where I can change the photos and their name.
The header needs to have these things.
- pictures of the golfer (use from pics attached)
- Their name
- Also under there name is smaller text I need a line of text you can just say "Offical Website" in your e.g to me
so for example you should have
Dale Fenwick
Offical Website
And some photos that are blended with some nice golf background or some grass or other ideas that you come up with that will look better than mine I'm sure :)
Size is 1000px x 120px
It needs to look professional and blend in nicely. I don't mind how many photos are used maybe 1-4?
The text needs to look professional too but not boring.
The header you create will be used on a website for a Professional Golfer (tour pro) their job is golf, their website needs to showcase them and promote them as best as possible.
As I said above I will need to swap photos easily and edit the text so will need the source files.
So a important point here. I guess there is no need to blend or do anything to the photos you add as I will actually need to change the photos and just need a simple template that I can swap photos and edit their name.
Ultimately I would like 3 versions of the header done and source files for all 3 so I can give them(the golfers) a choice of header type.
See how you go.
Remember that the header must have the ability for me to easily swap images and of course change the text.
My goal is to use the same header for each golfer but obviously with their images and their name.
I have CS5 so will need the source files photoshop, illustrator etc
2 example headers are attached to show you my attempts :) Please do something better.
I don't want any flash.

```html
<!DOCTYPE html>
<html lang="en">
<head>
<meta charset="utf-8">
<title>Dale Fenwick – Official Website Header</title>
<link href="https://fonts.googleapis.com/css2?family=Open+Sans:wght@400;600;700;800&display=swap" rel="stylesheet">
<style>
  :root {
    --bg-top: #9a9f9c;
    --bg-bottom: #7c817e;
    --band-navy: #0b1a2c;
    --band-navy-deep: #061120;
    --band-blue: #4f9fd8;
    --band-glow: #a9d6f3;
    --name-white: #ffffff;
    --tag-dark: #1b2228;
    --frame: #3d4a3a;
    --frame-light: #c6cbc4;
    --photo-face: #8c8a6a;
    --photo-swing: #6e8d5a;
    --photo-bunker: #7f8b4e;
  }
  html, body {
    margin: 0;
    padding: 0;
    width: 1200px;
    height: 144px;
    overflow: hidden;
  }
  .site-header {
    position: relative;
    width: 1200px;
    height: 144px;
    background: linear-gradient(180deg, var(--bg-top), var(--bg-bottom));
    font-family: "Open Sans", sans-serif;
    overflow: hidden;
  }
  .band {
    position: absolute;
    left: 0;
    top: 38px;
    width: 1200px;
    height: 72px;
  }
  .band__glow {
    position: absolute;
    left: 0; right: 0;
    top: 0;
    height: 16px;
    background: linear-gradient(180deg, var(--band-glow), var(--band-blue));
  }
  .band__body {
    position: absolute;
    left: 0; right: 0;
    top: 16px;
    height: 48px;
    background: linear-gradient(90deg, var(--band-navy-deep) 0%, var(--band-navy) 45%, #2f6fa6 60%, var(--band-blue) 100%);
  }
  .band__edge {
    position: absolute;
    left: 0; right: 0;
    top: 64px;
    height: 4px;
    background: linear-gradient(90deg, #2c5f86, #8cc4e8);
  }
  .golfer-name {
    position: absolute;
    left: 38px;
    top: 38px;
    margin: 0;
    color: var(--name-white);
    font-size: 54px;
    line-height: 72px;
    letter-spacing: -1px;
    text-transform: uppercase;
    white-space: nowrap;
  }
  .golfer-name__first { font-weight: 400; }
  .golfer-name__last { font-weight: 800; }
  .tagline {
    position: absolute;
    left: 198px;
    top: 107px;
    margin: 0;
    color: var(--tag-dark);
    font-size: 13px;
    font-weight: 700;
    letter-spacing: 0.5px;
  }
  .gallery {
    position: absolute;
    top: 10px;
    left: 566px;
    display: flex;
    gap: 21px;
  }
  .gallery__photo {
    width: 192px;
    height: 122px;
    box-sizing: border-box;
    border: 3px solid var(--frame);
    border-radius: 5px;
    box-shadow: 0 0 0 1px var(--frame-light), 0 2px 6px rgba(0,0,0,0.4);
  }
  .gallery__photo--portrait { background: linear-gradient(160deg, #a7a38a, var(--photo-face) 55%, #4f6a3a); }
  .gallery__photo--swing { background: linear-gradient(180deg, #5f7f4c, var(--photo-swing) 60%, #d8dcd6); }
  .gallery__photo--bunker { background: linear-gradient(200deg, #5d7a3a, var(--photo-bunker) 60%, #b9b08a); }
</style>
</head>
<body>
<header class="site-header">
  <div class="band">
    <div class="band__glow"></div>
    <div class="band__body"></div>
    <div class="band__edge"></div>
  </div>
  <h1 class="golfer-name"><span class="golfer-name__first">Dale</span><span class="golfer-name__last">Fenwick</span></h1>
  <p class="tagline">Offical Website</p>
  <div class="gallery">
    <div class="gallery__photo gallery__photo--portrait" role="img" aria-label="Close-up photo of the golfer wearing a white cap"></div>
    <div class="gallery__photo gallery__photo--swing" role="img" aria-label="Photo of the golfer finishing a swing on the tee"></div>
    <div class="gallery__photo gallery__photo--bunker" role="img" aria-label="Photo of the golfer playing a shot from the rough"></div>
  </div>
</header>
</body>
</html>
```